Zielgruppe
WIr sind ein klassisches Immobilienmaklerbüro für private Wohnimmobilien. Die Zielgruppe sind somit sowohl Verkäufer (i.d.R. gut situiert, 50-70 Jahre) als auch Käufer und Interessenten (20-35 Jahre).
Aufgabenstellung
Das Desgin soll seriös, vertrauenswürdig aber dennoch modern und dynamisch sein. Ich vollziehe aktuell einen Designwechsel und bin von einem schwarzen Design (www.wohn-punkt.example) auf ein helles Deisgn (http://wohnpunkt.de.xq48213.hostbeispiel.example/) umgestiegen. Die Visitenkarte soll zum neuen Design passen. Ein Bild von mir ist nicht gewünscht. Ob die Rückseite der Karten genutzt werden soll weiß ich selbst noch nicht. Wenn jemand eine sinnvolle Verwendung hat, bin ich dafür gerne offen.

```html
<!DOCTYPE html>
<html lang="de">
<head>
<meta charset="utf-8">
<title>Visitenkarte – WohnPunkt Immobilien</title>
<link rel="stylesheet" href="https://fonts.googleapis.com/css2?family=Open+Sans:wght@400;600;700&display=swap">
<style>
  :root {
    --page: #e6e6ea;
    --card: #f6f5f8;
    --green: #6fa82a;
    --text: #5a5a5e;
    --text-strong: #4a4a4e;
    --ink: #111111;
  }
  * { margin: 0; padding: 0; box-sizing: border-box; }
  html, body { width: 1200px; height: 1050px; overflow: hidden; }
  body {
    background: var(--page);
    font-family: "Open Sans", Arial, sans-serif;
    color: var(--text);
    position: relative;
  }
  .card {
    position: absolute;
    left: 120px; top: 215px;
    width: 960px; height: 620px;
    background: var(--card);
    box-shadow: 0 6px 24px rgba(0,0,0,.12);
  }
  .accent-block {
    position: absolute;
    left: 0; top: 42px;
    width: 112px; height: 70px;
    background: var(--green);
  }
  .holder { position: absolute; left: 140px; top: 40px; }
  .holder-name {
    font-size: 42px; font-weight: 700; color: var(--text-strong);
    line-height: 1.1;
  }
  .holder-role { font-size: 23px; margin-top: 4px; }
  .holder-role .divider { color: var(--green); margin: 0 6px; }
  .contact-list { list-style: none; position: absolute; font-size: 22px; line-height: 34px; }
  .contact-list li { display: flex; align-items: center; }
  .contact-list .icon { width: 18px; height: 18px; margin-right: 14px; flex: none; }
  .contact-list .indent { margin-left: 32px; }
  .company-contact { left: 108px; top: 152px; }
  .direct-contact { left: 520px; top: 440px; }
  .brand {
    position: absolute; right: 40px; top: 268px;
    display: flex; align-items: center;
  }
  .brand-name {
    font-size: 46px; font-weight: 400; color: var(--ink);
    letter-spacing: 9px; margin-right: 22px;
  }
  .brand-square { width: 92px; height: 92px; background: var(--ink); }
</style>
</head>
<body>
  <article class="card">
    <div class="accent-block"></div>
    <header class="holder">
      <h1 class="holder-name">Jonas Albrecht</h1>
      <p class="holder-role">Geschäftsführer<span class="divider">/</span>Betriebswirt (VWA)</p>
    </header>

    <ul class="contact-list company-contact">
      <li><svg class="icon" viewBox="0 0 18 18"><circle cx="9" cy="9" r="7" fill="none" stroke="var(--green)" stroke-width="3"/><circle cx="9" cy="9" r="2" fill="var(--green)"/></svg>WohnPunkt Immobilien GmbH</li>
      <li class="indent">Lindenstraße 14, 70173 Musterstadt</li>
      <li><svg class="icon" viewBox="0 0 18 18"><rect x="1" y="4" width="16" height="11" fill="var(--green)"/><path d="M1 4l8 6 8-6" fill="none" stroke="var(--card)" stroke-width="1.5"/></svg>info@wohn-punkt.example</li>
      <li><svg class="icon" viewBox="0 0 18 18"><circle cx="9" cy="9" r="8" fill="var(--green)"/><path d="M1 9h16M9 1c-4 4-4 12 0 16M9 1c4 4 4 12 0 16" fill="none" stroke="var(--card)" stroke-width="1.2"/></svg>www.wohn-punkt.example</li>
    </ul>

    <div class="brand">
      <span class="brand-name">WOHNPUNKT</span>
      <span class="brand-square"></span>
    </div>

    <ul class="contact-list direct-contact">
      <li><svg class="icon" viewBox="0 0 18 18"><path d="M4 1h4l1 4-2 2c1 2 2 3 4 4l2-2 4 1v4c-8 1-14-5-13-13z" fill="var(--green)"/></svg>0711 55012-23</li>
      <li><svg class="icon" viewBox="0 0 18 18"><rect x="2" y="7" width="14" height="9" rx="1" fill="var(--green)"/><rect x="4" y="2" width="10" height="5" fill="none" stroke="var(--green)" stroke-width="2"/></svg>0711 55012-24</li>
      <li><svg class="icon" viewBox="0 0 18 18"><rect x="5" y="1" width="8" height="16" rx="1.5" fill="var(--green)"/><rect x="7" y="3" width="4" height="9" fill="var(--card)"/></svg>0151 2847391</li>
      <li><svg class="icon" viewBox="0 0 18 18"><rect x="1" y="4" width="16" height="11" fill="var(--green)"/><path d="M1 4l8 6 8-6" fill="none" stroke="var(--card)" stroke-width="1.5"/></svg>albrecht@wohn-punkt.example</li>
    </ul>
  </article>
</body>
</html>
```